Eid Mubarak Digital Graphic

We seek designs for a digital greeting wishing our clients an Eid Mubarak. The graphic can contain Arabic and English text. This digital greeting should include our company logo.

Target Market(s)

Clients both commercial and government

Industry/Entity Type

Consulting

Font styles to use
Serif
Sans Serif
Decorative
Script
Other font styles liked:
• Arabic calligraphy

Requirements
Must have
• Digital graphic in a format easily sent by email and text
Company logo
Traditional Arabic greeting
Original graphic, not copied
Nice to have
• Arabic calligraphy
Should not have
• Nothing offensive to the Islamic religion

```html
<!DOCTYPE html>
<html lang="en">
<head>
<meta charset="utf-8">
<title>Eid Mubarak Greeting – Meridian Shield Advisory LLC</title>
<link rel="stylesheet" href="https://fonts.googleapis.com/css2?family=Great+Vibes&family=Playfair+Display:wght@700&display=swap">
<style>
  :root {
    --page: #ffffff;
    --navy: #0d2239;
    --navy-panel: #10263f;
    --lattice: #0b1e33;
    --gold: #c99a45;
    --gold-light: #e6c27a;
    --orange: #e8821c;
    --white: #ffffff;
  }
  html, body {
    margin: 0;
    padding: 0;
    width: 1200px;
    height: 1000px;
    overflow: hidden;
    background: var(--page);
  }
  .greeting-canvas {
    display: block;
    width: 1200px;
    height: 1000px;
  }
  .company-name {
    font-family: "Playfair Display", Georgia, serif;
    font-weight: 700;
    fill: var(--white);
    letter-spacing: 0.5px;
  }
  .headline-script {
    font-family: "Great Vibes", cursive;
    fill: var(--white);
  }
  .headline-caps {
    font-family: "Playfair Display", Georgia, serif;
    font-weight: 700;
    fill: var(--orange);
    letter-spacing: 1px;
  }
</style>
</head>
<body>
<svg class="greeting-canvas" viewBox="0 0 1200 1000" xmlns="http://www.w3.org/2000/svg" aria-label="Eid Mubarak greeting from Meridian Shield Advisory LLC">
  <defs>
    <filter id="card-shadow" x="-10%" y="-10%" width="130%" height="130%">
      <feDropShadow dx="8" dy="10" stdDeviation="9" flood-color="#000" flood-opacity="0.45"/>
    </filter>
    <filter id="panel-shadow" x="-20%" y="-10%" width="140%" height="130%">
      <feDropShadow dx="0" dy="6" stdDeviation="10" flood-color="#000" flood-opacity="0.5"/>
    </filter>
    <linearGradient id="gold-tone" x1="0" y1="0" x2="1" y2="1">
      <stop offset="0" stop-color="#e6c27a"/>
      <stop offset="0.5" stop-color="#c99a45"/>
      <stop offset="1" stop-color="#a87a30"/>
    </linearGradient>
  </defs>

  <rect class="card" x="175" y="75" width="852" height="852" fill="var(--navy)" filter="url(#card-shadow)"/>

  <path class="lace-frame" role="img" aria-label="Gold arabesque lace border forming an arch"
        d="M205 75 L205 600 A397 310 0 0 0 999 600 L999 75 L945 75 L945 600 A343 258 0 0 1 259 600 L259 75 Z"
        fill="url(#gold-tone)" opacity="0.85"/>

  <path class="lattice-field" role="img" aria-label="Islamic geometric lattice pattern"
        d="M262 75 L262 600 A340 255 0 0 0 942 600 L942 75 Z"
        fill="var(--lattice)"/>

  <g class="hanging-lines" stroke="var(--gold)" stroke-width="1.5">
    <line x1="255" y1="117" x2="425" y2="117" stroke-width="2"/>
    <line x1="777" y1="117" x2="945" y2="117" stroke-width="2"/>
    <line x1="333" y1="117" x2="333" y2="152"/>
    <line x1="866" y1="117" x2="866" y2="152"/>
    <line x1="287" y1="117" x2="287" y2="430"/>
    <line x1="912" y1="117" x2="912" y2="430"/>
  </g>

  <rect class="lantern" role="img" aria-label="Golden hanging lantern" x="312" y="152" width="42" height="108" rx="8" fill="url(#gold-tone)"/>
  <rect class="lantern" role="img" aria-label="Golden hanging lantern" x="845" y="152" width="42" height="108" rx="8" fill="url(#gold-tone)"/>
  <circle class="star" role="img" aria-label="Golden star ornament" cx="287" cy="457" r="27" fill="url(#gold-tone)"/>
  <circle class="star" role="img" aria-label="Golden star ornament" cx="912" cy="457" r="27" fill="url(#gold-tone)"/>

  <path class="center-panel" d="M372 75 L830 75 L830 546 A229 229 0 0 1 372 546 Z"
        fill="var(--navy-panel)" filter="url(#panel-shadow)"/>
  <path class="center-panel-rule" d="M381 75 L381 546 A220 220 0 0 0 821 546 L821 75"
        fill="none" stroke="var(--gold)" stroke-width="1.5" opacity="0.8"/>

  <text class="company-name" x="601" y="170" font-size="28" text-anchor="middle" textLength="380" lengthAdjust="spacingAndGlyphs">Meridian Shield Advisory LLC</text>

  <text class="headline-script" x="608" y="366" font-size="150" text-anchor="middle">Eid</text>
  <text class="headline-caps" x="601" y="427" font-size="58" text-anchor="middle" textLength="312" lengthAdjust="spacingAndGlyphs">MUBARAK</text>

  <line class="divider" x1="408" y1="469" x2="795" y2="469" stroke="var(--orange)" stroke-width="2"/>
  <line class="divider" x1="580" y1="486" x2="622" y2="486" stroke="var(--orange)" stroke-width="2"/>

  <rect class="calligraphy" role="img" aria-label="White Arabic calligraphy reading Eid Mubarak"
        x="508" y="540" width="190" height="180" rx="40" fill="var(--white)" opacity="0.85"/>
</svg>
</body>
</html>
```